Electrical contracting business specialising in smoke detector installation needs flyer design

i need a flyer design made up highlighting the fact that the Qld legislation is changing on smoke detectors in homes for everyones safety. I am an electrical contractor ( Tandrell Electrical) specialising in smoke detector installation to comply with the new Qld legislation. Some of the wording that can be used-
When you sleep, your sense of smell also sleeps. If a fire starts, toxic fumes canovercome you. Photoelectric smoke alarms see smoke and will alert you early, so you can escape. With interconnected alarms, you will be alerted no matter where you are, or where the fire starts.
New legislation specifies the type, positioning and interconnectedness of alarms, which are critical factors for an early warning and a quick escape.
To give your family the best chance of surviving a house fire, update your smoke alarms to match the new legislation as soon as you can. Call ME on 0418362957

Target Market(s)

Body Corporates , people selling and renting their properties

Industry/Entity Type

Electrician

Colors

Designer to choose colors to be used in the design.

Requirements
Must have
• Safety aspect.

```html
<!DOCTYPE html>
<html lang="en">
<head>
<meta charset="utf-8">
<title>Tandrell Electrical – Smoke Alarm Flyer</title>
<link href="https://fonts.googleapis.com/css2?family=Montserrat:wght@800;900&family=Lato:wght@400;700;900&family=Anton&display=swap" rel="stylesheet">
<style>
  :root {
    --stage: #15171c;
    --ink: #0b0b0c;
    --gold: #c0924f;
    --white: #ffffff;
    --paper: #f4f4f4;
    --steel: #6d6e72;
    --text-dark: #111111;
  }
  html, body {
    margin: 0;
    width: 1200px;
    height: 848px;
    overflow: hidden;
    background: var(--stage);
  }
  .flyer {
    position: absolute;
    left: 314px;
    top: 20px;
    width: 572px;
    height: 808px;
    background: var(--paper);
    overflow: hidden;
    font-family: "Lato", sans-serif;
  }
  .flyer-top {
    position: absolute;
    inset: 0 0 auto 0;
    height: 470px;
    background: var(--ink);
  }
  .headline {
    position: absolute;
    top: 26px;
    left: 0;
    right: 0;
    text-align: center;
    margin: 0;
    font-family: "Montserrat", sans-serif;
    font-weight: 900;
    text-transform: uppercase;
    line-height: 1.05;
  }
  .headline-main {
    display: block;
    color: var(--gold);
    font-size: 52px;
    letter-spacing: 1px;
  }
  .headline-sub {
    display: block;
    color: var(--white);
    font-size: 25px;
    margin-top: 6px;
  }
  .intro {
    position: absolute;
    top: 124px;
    left: 40px;
    right: 40px;
    margin: 0;
    text-align: center;
    color: var(--gold);
    font-size: 12.5px;
    line-height: 1.4;
  }
  .scene {
    position: absolute;
    top: 196px;
    left: 0;
    width: 572px;
    height: 274px;
    background:
      radial-gradient(ellipse at 60% 40%, rgba(90,200,230,0.45), transparent 55%),
      radial-gradient(ellipse at 20% 30%, rgba(200,120,60,0.35), transparent 45%),
      linear-gradient(180deg, #1f2226 0%, #3a3d42 60%, #2a2c30 100%);
  }
  .wave {
    position: absolute;
    top: 280px;
    left: 0;
    width: 572px;
    height: 200px;
  }
  .brand {
    position: absolute;
    top: 356px;
    left: 34px;
    display: flex;
    align-items: center;
    gap: 10px;
  }
  .brand-mark {
    width: 18px;
    height: 18px;
    background: var(--gold);
  }
  .brand-name {
    font-weight: 900;
    font-size: 26px;
    line-height: 1;
    color: var(--gold);
  }
  .brand-owner {
    position: absolute;
    top: 392px;
    left: 62px;
    margin: 0;
    color: var(--gold);
    font-size: 14px;
    line-height: 1.3;
  }
  .legislation {
    position: absolute;
    top: 472px;
    left: 30px;
    right: 30px;
    margin: 0;
    padding: 14px 30px;
    background: var(--gold);
    border-radius: 40px;
    color: var(--white);
    font-weight: 700;
    font-size: 15px;
    line-height: 1.35;
    text-align: center;
  }
  .advice {
    position: absolute;
    top: 578px;
    left: 40px;
    right: 40px;
    margin: 0;
    color: var(--text-dark);
    font-weight: 900;
    font-size: 14.5px;
    line-height: 1.35;
  }
  .call {
    position: absolute;
    top: 636px;
    left: 36px;
    right: 36px;
    margin: 0;
    font-family: "Anton", sans-serif;
    font-size: 54px;
    line-height: 1.1;
    white-space: nowrap;
    color: var(--text-dark);
    letter-spacing: 1px;
  }
  .footer-band {
    position: absolute;
    left: 0;
    right: 0;
    bottom: 0;
    height: 52px;
    background: var(--gold);
  }
</style>
</head>
<body>
  <main class="flyer">
    <section class="flyer-top">
      <h1 class="headline">
        <span class="headline-main">When you sleep</span>
        <span class="headline-sub">Your sense of smell also sleeps.</span>
      </h1>
      <p class="intro">If a fire starts, toxic fumes can overcome you. Photoelectric smoke alarms see smoke and will alert you early, so you can escape. With interconnected alarms, you will be alerted no matter where you are, or where the fire starts.</p>
      <div class="scene" role="img" aria-label="Night-time home interior with ceiling smoke alarms casting blue detection cones, linked together, as smoke rises from a kitchen"></div>
    </section>

    <svg class="wave" viewBox="0 0 572 200" preserveAspectRatio="none" aria-hidden="true">
      <path d="M0 20 C 180 0, 280 30, 380 100 S 530 180, 572 170 L572 200 L0 200 Z" fill="var(--paper)"/>
      <path d="M0 20 C 180 0, 280 30, 380 100 S 530 180, 572 170" fill="none" stroke="var(--gold)" stroke-width="5"/>
      <path d="M0 30 C 185 10, 288 42, 388 112 S 535 192, 572 182" fill="none" stroke="var(--steel)" stroke-width="5"/>
      <path d="M0 40 C 190 20, 296 54, 396 124 S 540 204, 572 194" fill="none" stroke="var(--gold)" stroke-width="2"/>
    </svg>

    <div class="brand">
      <span class="brand-mark"></span>
      <span class="brand-name">Tandrell Electrical</span>
    </div>
    <p class="brand-owner">Dane Tandrell<br>Electrical Contractor</p>

    <p class="legislation">New legislation specifies the type, positioning and interconnectedness of alarms, which are critical factors for an early warning and a quick escape.</p>

    <p class="advice">To give your family the best chance of surviving a house fire, update your smoke alarms to match the new legislation as soon as you can.</p>

    <p class="call">CALL @: 0418362957</p>

    <div class="footer-band"></div>
  </main>
</body>
</html>
```